Darin Wekel Orthodontics
Business Card, Letterhead, Envelopes, Folder
@ Project holder : Please,Extend this Contest.
I am interested and Coming....
Anyone do a full size envelope where the letterhead slides in the envelope unfolded.
Anyone willing to experiment by putting the log and info at the bottom of the stationary page rather than the top.
Thanks for your submissions.#2,3,6,7 appear too busy for me. Lets stick with simplicity. Back of business card should probably have a white or light background so we can write the appoitment time in pen on the card.
ai format uploaded
kindly upload ai or eps file of logo

```html
<!DOCTYPE html>
<html lang="en">
<head>
<meta charset="utf-8">
<title>Darin Wekel Orthodontics – Stationery Set</title>
<link href="https://fonts.googleapis.com/css2?family=Raleway:wght@300;400&display=swap" rel="stylesheet">
<style>
  :root{
    --navy-deep:#0b2252;
    --navy-mid:#1a4486;
    --navy-light:#3569b4;
    --paper:#ffffff;
    --line:#c9ced8;
    --ink:#5b6170;
    --ink-light:#ffffff;
    --ghost:#e9ecf2;
    --canvas:#ffffff;
    --shadow:rgba(0,0,0,.18);
  }
  *{box-sizing:border-box;margin:0;padding:0}
  html,body{width:1200px;height:334px;overflow:hidden;background:var(--canvas)}
  body{position:relative;font-family:"Raleway",Arial,sans-serif}
  .piece{position:absolute;box-shadow:0 1px 3px var(--shadow)}
  .blue{background:radial-gradient(ellipse at 50% 45%,var(--navy-light) 0%,var(--navy-mid) 40%,var(--navy-deep) 100%)}
  .white{background:var(--paper);border:1px solid var(--line)}
  .brand{color:var(--ink-light);font-weight:300;text-align:center;line-height:1}
  .brand .name{display:block;letter-spacing:.5px}
  .brand .sub{display:block;letter-spacing:2px;margin-top:3px}
  .contact{color:var(--ink-light);font-size:5px;line-height:1.5;font-weight:400}

  /* Folder */
  .folder-cover{left:86px;top:7px;width:117px;height:154px}
  .folder-front{left:208px;top:7px;width:121px;height:154px}
  .folder-front .brand{position:absolute;top:50px;left:0;right:0}
  .folder-front .name{font-size:17px}
  .folder-front .sub{font-size:5px}
  .folder-inside{top:168px;width:117px;height:161px}
  .folder-inside.left{left:86px}
  .folder-inside.right{left:208px;width:121px}
  .pocket-tab{position:absolute;bottom:10px;width:40px;height:38px;border-radius:0 0 8px 8px}
  .folder-inside.left .pocket-tab{right:10px}
  .folder-inside.right .pocket-tab{left:10px}

  /* Business card */
  .card-front{left:396px;top:12px;width:204px;height:120px}
  .card-front .brand{position:absolute;top:22px;left:0;right:0}
  .card-front .name{font-size:18px}
  .card-front .sub{font-size:5px}
  .card-front .contact{position:absolute;left:16px;bottom:14px}
  .card-back{left:612px;top:12px;width:211px;height:120px;padding:16px 18px}
  .card-back .title{font-size:7px;color:var(--ink);margin-bottom:10px}
  .card-back .row{display:flex;align-items:flex-end;gap:6px;font-size:6px;color:var(--ink);margin-bottom:12px}
  .card-back .rule{flex:1;border-bottom:1px solid var(--line)}

  /* Envelope */
  .envelope{left:396px;top:151px;width:427px;height:173px;overflow:hidden}
  .envelope .flap{position:absolute;left:0;top:0;width:100%;height:60px}
  .envelope .brand{position:absolute;top:62px;left:0;right:0}
  .envelope .name{font-size:26px}
  .envelope .sub{font-size:6px}
  .envelope .contact{position:absolute;left:22px;bottom:16px}

  /* Letterhead */
  .letterhead{left:854px;top:7px;width:262px;height:322px}
  .letterhead .brand{position:absolute;top:18px;left:0;right:0;color:var(--navy-mid)}
  .letterhead .name{font-size:20px}
  .letterhead .sub{font-size:5px}
  .letterhead .ghost{position:absolute;top:138px;left:0;right:0;text-align:center;color:var(--ghost);font-weight:300}
  .letterhead .ghost .name{font-size:34px}
  .letterhead .ghost .sub{font-size:8px;letter-spacing:3px}
  .letterhead .contact{position:absolute;bottom:12px;left:0;right:0;text-align:center;color:var(--ink)}
</style>
</head>
<body>
  <!-- Folder exterior -->
  <div class="piece blue folder-cover"></div>
  <div class="piece blue folder-front">
    <div class="brand"><span class="name">Darin Wekel</span><span class="sub">ORTHODONTICS</span></div>
  </div>
  <!-- Folder interior -->
  <div class="piece white folder-inside left"><div class="pocket-tab blue"></div></div>
  <div class="piece white folder-inside right"><div class="pocket-tab blue"></div></div>

  <!-- Business card -->
  <div class="piece blue card-front">
    <div class="brand"><span class="name">Darin Wekel</span><span class="sub">ORTHODONTICS</span></div>
    <div class="contact">Darin Wekel, DDS<br>120 Maple Ave, Fairview<br>T 555 0142</div>
  </div>
  <div class="piece white card-back">
    <p class="title">Your next appointment</p>
    <div class="row">Date <span class="rule"></span></div>
    <div class="row">Time <span class="rule"></span></div>
  </div>

  <!-- Envelope -->
  <div class="piece blue envelope">
    <svg class="flap" viewBox="0 0 427 60" preserveAspectRatio="none" aria-hidden="true">
      <path d="M0 0 H427 V28 Q427 52 395 52 H32 Q0 52 0 28 Z" fill="none" stroke="rgba(255,255,255,.18)" stroke-width="1"/>
    </svg>
    <div class="brand"><span class="name">Darin Wekel</span><span class="sub">ORTHODONTICS</span></div>
    <div class="contact">120 Maple Ave, Suite 4<br>Fairview, CA 90210</div>
  </div>

  <!-- Letterhead -->
  <div class="piece white letterhead">
    <div class="brand"><span class="name">Darin Wekel</span><span class="sub">ORTHODONTICS</span></div>
    <div class="ghost" aria-hidden="true"><span class="name">Darin Wekel</span><span class="sub">ORTHODONTICS</span></div>
    <div class="contact">120 Maple Ave, Suite 4, Fairview<br>T 555 0142 · info@darinwekel.com</div>
  </div>
</body>
</html>
```